Property Developer - Simple yet Sophisticated and Sharp Business Card

We are a medium sized property developer involved mainly in townhouse developments and land subdivisions.

The company is looking for a simple, sharp and sophisticated business card that will be given to contractors, land owners, financiers etc and thus will need to look professional.

Property development related graphics and art can be used, however the card is not to be too "busy" or crowded. Our company name is KL Estates which could possibly be incorporated into the graphics or artwork.

Single sided and/or double sided designs will be acceptable.

A Simple, Sophisticated, Sharp design please!

Good Luck !

```html
<!DOCTYPE html>
<html lang="en">
<head>
<meta charset="utf-8">
<title>KL Estates – Business Card</title>
<link rel="stylesheet" href="https://fonts.googleapis.com/css2?family=Roboto:wght@400;700&display=swap">
<style>
  :root {
    --brand-blue: #3b7bfb;
    --card-white: #ffffff;
    --backdrop: #eeeff1;
    --card-edge: #d9dbe0;
    --text-on-blue: #ffffff;
  }
  * { margin: 0; padding: 0; box-sizing: border-box; }
  html, body {
    width: 1200px;
    height: 900px;
    overflow: hidden;
    background: var(--backdrop);
    font-family: "Roboto", Arial, sans-serif;
  }
  .canvas {
    position: relative;
    width: 1200px;
    height: 900px;
  }
  .card {
    position: absolute;
    width: 662px;
    height: 404px;
  }
  .card--contact {
    left: 34px;
    top: 28px;
    background: var(--brand-blue);
  }
  .contact-list {
    position: absolute;
    left: 52px;
    top: 256px;
    list-style: none;
    color: var(--text-on-blue);
    font-size: 17px;
    font-weight: 400;
    line-height: 21px;
    letter-spacing: 0.2px;
  }
  .card--brand {
    left: 506px;
    top: 462px;
    background: var(--card-white);
    border: 1px solid var(--card-edge);
  }
  .brand-name {
    position: absolute;
    left: 72px;
    top: 148px;
    color: var(--brand-blue);
    font-size: 84px;
    font-weight: 700;
    line-height: 1;
    letter-spacing: -1px;
    text-transform: uppercase;
    white-space: nowrap;
  }
</style>
</head>
<body>
  <main class="canvas">
    <section class="card card--contact" aria-label="Card front: contact details">
      <ul class="contact-list">
        <li>ph: (07) 3000 1842</li>
        <li>F: (07) 3000 1843</li>
        <li>e: projects.klestates@mailbox.net</li>
        <li>PO Box 2486</li>
        <li>Hillcrest Vale QLD 4120</li>
      </ul>
    </section>
    <section class="card card--brand" aria-label="Card back: company name">
      <h1 class="brand-name">KL Estates</h1>
    </section>
  </main>
</body>
</html>
```